Bluewater Motor Finance Home Page

We need a desktop version mock up (we will base our mobile version off of this) of a website homepage for our auto loan business, Bluewater Motor Finance. This does not need to be a functioning site, just a home page mock up. We are based in the metro St. Louis, MO area. We offer "guaranteed" auto loans for all credit types. We specialize in financing for bad/no credit customers. We are able to help rebuild these type of customers' credit, all while putting them in a great late model vehicle they'll love. Our online credit app takes less than 60 seconds, doesn't require a SS# and gives a free credit score if they fill it out within 3 minutes. We are looking for an outside perspective to help us in this design process. We are not completely sure what we want, but we do want it to be professional and secure looking, all while being unique and aesthetically pleasing. We want the customer to be able to put in their zip code to be directed to the right location that can get them pre approved. I attached a wireframe with some stuff we'd like to include, but in no way does it have to be in the same layout or the same ideas. We want everyone to "go crazy" with their creative side on this. Our current site is awful, here is a link to get a better idea: www.bluewatermotorfinance-example.com. Attached is our logo too, base colors off of it. Watch our video that is also attached for a better idea.

Target Market(s)

Residents of the St. Louis Missouri Metro Area that need an auto loan. 24-55 Male and Female - Lots of "urban market" customers.

Industry/Entity Type

Loan

Number of Pages Required

1 page

Colors
9bcb3b

Requirements
Must have
• An area where the customer can enter their zip code - Be creative!
Nice to have
• See wireframe attachment for ideas - Be creative!

```html
<!DOCTYPE html>
<html lang="en">
<head>
<meta charset="utf-8">
<title>Bluewater Motor Finance — Home</title>
<link rel="stylesheet" href="https://fonts.googleapis.com/css2?family=Arimo:wght@400;700&family=Cabin:wght@400;500&family=Tinos&display=swap">
<style>
  :root{
    --brand-green:#9bcb3b;
    --nav-green:#6fbf3f;
    --cta-yellow:#f5ec0c;
    --title-yellow:#f3e81a;
    --ink:#111;
    --white:#fff;
    --black:#000;
    --panel-grey:rgba(190,190,190,.55);
  }
  *{box-sizing:border-box;margin:0;padding:0}
  html,body{width:1200px;height:2475px;overflow:hidden}
  body{position:relative;font-family:"Arimo",Arial,sans-serif;color:var(--ink);background:var(--white)}
  .abs{position:absolute}

  /* Hero */
  .hero{position:absolute;left:0;top:0;width:1200px;height:800px;overflow:hidden;
    background:linear-gradient(180deg,#7d7f72 0%,#a9a58e 22%,#6f6d4e 40%,#5b5a44 60%,#4e4c3c 100%)}
  .hero-photo{position:absolute;inset:0;
    background:radial-gradient(ellipse 360px 300px at 180px 560px,#7e9a4a 0%,rgba(110,140,60,.6) 45%,rgba(0,0,0,0) 100%),
               radial-gradient(ellipse 500px 260px at 880px 300px,rgba(210,205,185,.5),rgba(0,0,0,0))}
  .brand{position:absolute;left:21px;top:44px;display:flex;align-items:center;gap:14px}
  .brand-mark{width:60px;height:60px;background:var(--brand-green)}
  .brand-name{font-family:"Arimo",Arial,sans-serif;font-weight:700;font-size:38px;color:var(--brand-green);line-height:1}
  .nav{position:absolute;left:400px;top:178px;width:800px;height:70px;background:rgba(238,238,238,.93)}
  .nav a{position:absolute;top:19px;font-size:27px;color:var(--ink);text-decoration:none;line-height:1}
  .nav a.current{color:var(--nav-green)}
  .headline{position:absolute;left:0;width:1200px;top:362px;text-align:center;font-family:"Cabin",sans-serif;
    font-size:60px;color:var(--white);text-shadow:2px 2px 2px #000,0 0 3px #000}
  .subline{position:absolute;left:0;width:1200px;top:439px;text-align:center;font-family:"Cabin",sans-serif;
    font-size:34px;color:var(--white);text-shadow:2px 2px 2px #000}
  .zip-form{position:absolute;left:285px;top:519px;width:476px;height:84px;background:var(--brand-green)}
  .zip-input,.zip-submit{position:absolute;top:11px;height:56px;background:var(--white);font-size:27px;
    display:flex;align-items:center;justify-content:center;color:var(--ink)}
  .zip-input{left:17px;width:210px}
  .zip-submit{left:247px;width:211px}
  .perks{position:absolute;left:765px;top:519px;width:335px;height:86px;background:var(--black);padding:2px 0 0 3px;list-style:none}
  .perks li{display:flex;align-items:center;gap:4px;color:var(--white);font-size:16px;line-height:21.5px}
  .perks svg{flex:none}
  .timer-line{position:absolute;left:0;width:1200px;top:759px;height:41px;display:flex;justify-content:center;align-items:center;gap:12px;
    color:var(--white);font-size:21px}
  .timer{width:72px;height:41px;background:var(--black);border:1px solid #ccc;display:flex;align-items:center;justify-content:center}

  /* Testimonial */
  .testimonials{position:absolute;left:0;top:800px;width:1200px;height:572px;overflow:hidden;
    background:linear-gradient(180deg,#dbe9ef 0%,#cfe0c8 40%,#bcd3a6 62%,#c9cfcf 82%,#b9b9b9 100%)}
  .testimonial-title{position:absolute;left:0;width:1184px;top:80px;text-align:center;font-size:43px;color:var(--title-yellow);
    -webkit-text-stroke:1px #333;text-shadow:2px 2px 1px #222}
  .testimonial-quote{position:absolute;left:100px;width:1030px;top:156px;text-align:center;font-size:21px;line-height:27px}
  .testimonial-author{position:absolute;left:0;width:1184px;top:234px;text-align:center;font-size:26px;color:var(--title-yellow);
    -webkit-text-stroke:.6px #556b1a}
  .arrow{position:absolute}
  .payment-copy{position:absolute;left:100px;width:722px;top:388px;text-align:center;font-size:28px;line-height:34px}
  .payment-button{position:absolute;left:841px;top:392px;width:250px;height:68px;background:var(--cta-yellow);border:2px solid #222;
    display:flex;align-items:center;justify-content:center;font-size:23px}

  /* Steps */
  .steps{position:absolute;left:0;top:1372px;width:1200px;height:910px;overflow:hidden;font-family:"Tinos",serif;color:var(--white);
    background:radial-gradient(ellipse 700px 500px at 560px 420px,#8eaa6e 0%,#5f8a48 45%,#2d6a2a 80%,#1f5a22 100%)}
  .step{position:absolute;width:650px;text-align:center;font-size:21px;line-height:25.5px}
  .frame{position:absolute;border:2px solid rgba(255,255,255,.85);background:var(--panel-grey)}
  .about-title{position:absolute;left:35px;top:650px;font-family:"Arimo",Arial,sans-serif;font-weight:700;font-size:29px;color:var(--brand-green)}
  .about-copy{position:absolute;left:66px;top:690px;width:640px;font-size:21px;line-height:25.4px}
  .video{position:absolute;left:746px;top:660px;width:325px;height:209px;border:3px solid var(--white);background:rgba(120,150,100,.35)}

  /* Footer */
  .footer{position:absolute;left:0;top:2282px;width:1200px;height:193px;background:var(--black);color:var(--white);text-align:center}
  .footer-links{position:absolute;left:0;width:1200px;top:58px;display:flex;justify-content:center;gap:24px;font-size:21px}
  .footer-links a{color:var(--white);text-decoration:none}
  .footer-legal{position:absolute;left:0;width:1200px;top:110px;font-size:20px;line-height:25px}
</style>
</head>
<body>

<header class="hero">
  <div class="hero-photo" role="img" aria-label="Photo of a green hatchback driving down a tree-lined road toward a city skyline"></div>
  <div class="brand"><span class="brand-mark"></span><span class="brand-name">Bluewater Motor Finance</span></div>
  <nav class="nav">
    <a class="current" style="left:25px">Locations</a>
    <a style="left:179px">Finance Center</a>
    <a style="left:415px">About</a>
    <a style="left:529px;top:22px">FAQ</a>
    <a style="left:626px">Contact</a>
  </nav>
  <h1 class="headline">Over 30,000 Auto Loans Since 2000</h1>
  <p class="subline">Pre-Approval in Under 60 Seconds!</p>
  <div class="zip-form">
    <div class="zip-input">Enter zip code</div>
    <div class="zip-submit">Get Approved</div>
  </div>
  <ul class="perks">
    <li><svg width="14" height="14" viewBox="0 0 14 14"><circle cx="7" cy="7" r="7" fill="#3fae3a"/><path d="M3.5 7.2l2.3 2.3 4.7-5" stroke="#fff" stroke-width="2" fill="none"/></svg>No Social Security Number Required</li>
    <li><svg width="14" height="14" viewBox="0 0 14 14"><circle cx="7" cy="7" r="7" fill="#3fae3a"/><path d="M3.5 7.2l2.3 2.3 4.7-5" stroke="#fff" stroke-width="2" fill="none"/></svg>Instant Approval</li>
    <li><svg width="14" height="14" viewBox="0 0 14 14"><circle cx="7" cy="7" r="7" fill="#3fae3a"/><path d="M3.5 7.2l2.3 2.3 4.7-5" stroke="#fff" stroke-width="2" fill="none"/></svg>No Application Fees</li>
    <li><svg width="14" height="14" viewBox="0 0 14 14"><circle cx="7" cy="7" r="7" fill="#3fae3a"/><path d="M3.5 7.2l2.3 2.3 4.7-5" stroke="#fff" stroke-width="2" fill="none"/></svg>All Credit Accepted</li>
  </ul>
  <div class="timer-line"><span>Apply within</span><span class="timer">3:00</span><span>and see your credit score for free!</span></div>
</header>

<section class="testimonials" role="img" aria-label="Soft illustration of a green city street with trees, buildings and cars">
  <h2 class="testimonial-title">Testimonial</h2>
  <svg class="arrow" style="left:50px;top:130px" width="32" height="42" viewBox="0 0 32 42"><path d="M32 0V42L0 21Z" fill="#000"/></svg>
  <svg class="arrow" style="left:1136px;top:132px" width="41" height="48" viewBox="0 0 41 48"><path d="M0 0V48L41 24Z" fill="#000"/></svg>
  <p class="testimonial-quote">Lorem ipsum dolor sit amet, consectetur adipiscing elit. Proin a elit vitae erat accumsan venenatis in e?citur velit. dapibus fringilla!</p>
  <p class="testimonial-author">Satisfid Customer</p>
  <p class="payment-copy">Lorem ipsum dolor sit amet, consectetur adipiscing elit.<br>Proin a elit vitae erat accumsan.</p>
  <div class="payment-button">Calculate Payment</div>
</section>

<section class="steps" role="img" aria-label="Green backdrop with a faint world map and soft bokeh lights">
  <div class="step" style="left:57px;top:21px">Step 1<br>Lorem ipsum dolor sit amet, consectetur adipiscing elit. Proin a elit vitae erat accumsan venenatis in e?citur velit. dapibus fringilla. Nulla varius eleifend risus non scelerisque. Morbi sapien lorem, gravida in ex in, ?nibus scelerisque massa. Quisque in vulputate magna.</div>
  <div class="frame" style="left:743px;top:38px;width:324px;height:134px"></div>
  <div class="frame" style="left:168px;top:243px;width:325px;height:133px"></div>
  <div class="step" style="left:522px;top:229px">Step 2<br>Lorem ipsum dolor sit amet, consectetur adipiscing elit. Proin a elit vitae erat accumsan venenatis in e?citur velit. dapibus fringilla. Nulla varius eleifend risus non scelerisque. Morbi sapien lorem, gravida in ex in, ?nibus scelerisque massa. Quisque in vulputate magna.</div>
  <div class="step" style="left:57px;top:432px">Step 3<br>Lorem ipsum dolor sit amet, consectetur adipiscing elit. Proin a elit vitae erat accumsan venenatis in e?citur velit. dapibus fringilla. Nulla varius eleifend risus non scelerisque. Morbi sapien lorem, gravida in ex in, ?nibus scelerisque massa. Quisque in vulputate magna.</div>
  <div class="frame" style="left:747px;top:447px;width:323px;height:132px"></div>
  <h2 class="about-title">Bluewater Motor Finance</h2>
  <p class="about-copy">Lorem ipsum dolor sit amet, consectetur adipiscing elit.<br>Proin a elit vitae erat accumsan venenatis in<br>e?citur velit. dapibus fringilla! Lorem ipsum dolor sit amet,<br>consectetur adipiscing elit. Proin a elit vitae erat accumsan<br>venenatis in e?citur velit. dapibus fringilla.<br>Nulla varius eleifend risus non scelerisque. Morbi<br>sapien lorem, gravida in ex in, ?nibus scelerisque massa.<br>Quisque in vulputate magna.</p>
  <div class="video">
    <svg style="position:absolute;left:110px;top:52px" width="104" height="96" viewBox="0 0 104 96"><ellipse cx="52" cy="48" rx="50" ry="46" fill="none" stroke="#fff" stroke-width="2"/><path d="M40 26V70L78 48Z" fill="#fff"/></svg>
  </div>
</section>

<footer class="footer">
  <nav class="footer-links"><a>HOME</a><a>ABOUT</a><a>PRIVACY</a><a>CONTACT</a></nav>
  <p class="footer-legal">© 2016 Bluewater Motor Finance. All Rights Reserved.<br>Created by Northfield Studio.</p>
</footer>

</body>
</html>
```